BrackenVale Construction

We need to do a design with our logo on our cars. Both of the directors have Morvane kestra utes.

Target Market(s)

just advertising

Industry/Entity Type

Building

Font styles to use
Sans Serif
Script

Colors
0255a3
3176b5
85acd3
cfdeed
ffffff

Requirements
Must have
• signage on the side of the car and the back tailgate.
Nice to have
• our website(currently being upgraded) numbers aren't super important but id like our name and the words " A professional approach to quality construction" (See website)

```html
<!DOCTYPE html>
<html lang="en">
<head>
<meta charset="utf-8">
<title>BrackenVale Construction – Vehicle Signage</title>
<link href="https://fonts.googleapis.com/css2?family=Gelasio:wght@400&family=Open+Sans:wght@400&display=swap" rel="stylesheet">
<style>
  :root {
    --page-bg: #e6e6e6;
    --sign-white: #ffffff;
    --brand-blue: #1d4aa0;
    --ink: #111114;
    --stone-dark: #6f6a62;
    --stone-mid: #8e877c;
    --stone-light: #a59d90;
  }
  html, body {
    margin: 0;
    padding: 0;
    width: 1200px;
    height: 1200px;
    overflow: hidden;
    background: var(--page-bg);
  }
  .canvas {
    position: relative;
    width: 1200px;
    height: 1200px;
  }
  .sign {
    position: absolute;
    background: var(--sign-white);
    overflow: hidden;
  }
  .sign--side { left: 42px; top: 96px; width: 1110px; height: 418px; }
  .sign--tailgate { left: 228px; top: 590px; width: 738px; height: 550px; }

  .stone-band {
    position: absolute;
    left: 0; top: 0; width: 100%;
    background: linear-gradient(180deg, var(--stone-light) 0%, var(--stone-mid) 50%, var(--stone-dark) 100%);
  }
  .sign--side .stone-band { height: 78px; }
  .sign--tailgate .stone-band { height: 160px; }

  .web-band {
    position: absolute;
    left: 0; bottom: 0; width: 100%;
    background: var(--brand-blue);
    color: var(--sign-white);
    font-family: "Open Sans", sans-serif;
    text-align: center;
    white-space: nowrap;
  }
  .sign--side .web-band { height: 82px; line-height: 80px; font-size: 54px; }
  .sign--tailgate .web-band { height: 74px; line-height: 72px; font-size: 40px; }

  .brand-square {
    position: absolute;
    background: var(--brand-blue);
  }
  .sign--side .brand-square { left: 88px; top: 124px; width: 196px; height: 184px; }
  .sign--tailgate .brand-square { left: 18px; top: 182px; width: 292px; height: 272px; }

  .company-name {
    position: absolute;
    margin: 0;
    font-family: "Gelasio", Georgia, serif;
    font-weight: 400;
    color: var(--ink);
    white-space: nowrap;
    line-height: 1.1;
  }
  .sign--side .company-name { left: 314px; top: 112px; font-size: 50px; }
  .sign--tailgate .company-name { left: 331px; top: 218px; font-size: 56px; line-height: 70px; }

  .tagline {
    position: absolute;
    margin: 0;
    font-family: "Open Sans", sans-serif;
    color: var(--ink);
    line-height: 1.3;
  }
  .sign--side .tagline { left: 320px; top: 228px; font-size: 22px; white-space: nowrap; }
  .sign--tailgate .tagline { left: 334px; top: 366px; font-size: 23px; line-height: 32px; }
</style>
</head>
<body>
<main class="canvas">

  <section class="sign sign--side" aria-label="Side door sign">
    <div class="stone-band" role="img" aria-label="Stacked stone wall texture"></div>
    <div class="brand-square" aria-hidden="true"></div>
    <h1 class="company-name">BrackenVale Construction</h1>
    <p class="tagline">A professional approach to quality construction and design</p>
    <div class="web-band">www.brackenvaleconstruction.com.au</div>
  </section>

  <section class="sign sign--tailgate" aria-label="Tailgate sign">
    <div class="stone-band" role="img" aria-label="Stacked stone wall texture"></div>
    <div class="brand-square" aria-hidden="true"></div>
    <h2 class="company-name">BrackenVale<br>Construction</h2>
    <p class="tagline">A professional approach to<br>quality construction and design</p>
    <div class="web-band">www.brackenvaleconstruction.com.au</div>
  </section>

</main>
</body>
</html>
```